Prominent Law Firm Needs a New Stationary Design

We need new stationary design to go with our new logo and rustic offices.
Things we need on the letterhead:
logo (see attached file), would also like the Seven-Figure Verdict Logo (attached) somewhere on the stationary,
5182 North Pelham Avenue
Tulsa, Oklahoma 74219
(918) 555-0143 Tel ★ (918) 555-0187 Fax
www.TWVQX.example

We also need the names of the 4 partners:
Dale K. Hollingsworth
Vernon P. Hollingsworth
Mark E. Fenwicke
Tyler D. Ashcombe

And the other staff:
Brenda K. Lyle
Tendaji K. Oyelowanta
Gordon Pettijo

Hilda V. Pruitt, RN

Of Counsel:
Wendell S. Hollingsworth

Industry/Entity Type

Law Firm

```html
<!DOCTYPE html>
<html lang="en">
<head>
<meta charset="utf-8">
<title>Hollingsworth Hollingsworth Fenwicke – Stationery</title>
<link href="https://fonts.googleapis.com/css2?family=Questrial&display=swap" rel="stylesheet">
<style>
  :root{
    --backdrop:#d4d4d4;
    --ink:#1c1c1c;
    --paper:#f7f7f7;
    --dark:#262626;
    --rule:#9a9a9a;
    --muted:#444;
    --sig:#3a4fb0;
  }
  *{box-sizing:border-box;margin:0;padding:0}
  html,body{width:1200px;height:1000px;overflow:hidden}
  body{background:var(--backdrop);font-family:"Questrial",sans-serif;color:var(--ink);position:relative}
  .sheet{position:absolute}
  .brand{position:absolute;left:0;right:0;text-align:center;text-transform:uppercase;letter-spacing:.08em;line-height:1.25}
  .brand-dot{display:block;margin:0 auto 5px;border-radius:50%}

  /* Presentation folder */
  .folder{left:152px;top:42px;width:431px;height:558px;background:var(--dark);border-radius:4px}
  .folder-spine{position:absolute;left:19px;top:0;bottom:0;width:1px;background:#3a3a3a}
  .folder .brand{top:88px;color:#fff;font-size:16px;padding:0 90px}
  .folder .brand-dot{width:10px;height:10px;background:#fff}
  .folder-web{position:absolute;left:0;right:0;bottom:28px;text-align:center;color:#fff;font-size:10px;letter-spacing:.04em}

  /* Letterhead */
  .letterhead{left:616px;top:62px;width:417px;height:538px;background:var(--paper)}
  .letterhead .brand{top:26px;font-size:11px;padding:0 110px}
  .letterhead .brand-dot{width:8px;height:8px;background:var(--ink)}
  .letter-body{position:absolute;left:34px;right:34px;top:188px;font-size:6.2px;line-height:1.45;color:var(--ink)}
  .letter-body p{margin-bottom:7px;text-align:justify}
  .letter-close{margin-top:10px}
  .letter-close strong{display:block}
  .signature{position:absolute;left:92px;top:372px;width:76px;height:28px;background:linear-gradient(90deg,rgba(58,79,176,.15),rgba(58,79,176,.35))}
  .letter-footer{position:absolute;left:34px;right:34px;bottom:14px;display:flex;font-size:5.6px;line-height:1.45;color:var(--muted)}
  .letter-footer .col{flex:1;padding:0 8px;border-left:1px solid var(--rule)}
  .letter-footer .col:first-child{border-left:none;padding-left:0}
  .letter-footer b{color:var(--ink)}

  /* Envelopes */
  .envelope-front{left:117px;top:630px;width:466px;height:200px;background:var(--paper)}
  .envelope-front .brand{left:20px;right:auto;width:150px;top:22px;font-size:10px}
  .envelope-front .brand-dot{width:8px;height:8px;background:var(--ink)}
  .envelope-address{position:absolute;left:40px;top:178px;font-size:6px;line-height:1.4;color:var(--muted)}
  .envelope-back{left:616px;top:630px;width:467px;height:200px;background:var(--paper)}
  .envelope-back svg{position:absolute;left:0;top:0}
  .envelope-back .brand{top:12px;color:#fff;font-size:7px;padding:0 175px}
  .envelope-back .brand-dot{width:6px;height:6px;background:#fff;margin-bottom:3px}

  /* Business cards */
  .card-front{left:410px;top:860px;width:180px;height:100px;background:var(--dark)}
  .card-front .brand{top:22px;color:#fff;font-size:7px;padding:0 28px}
  .card-front .brand-dot{width:6px;height:6px;background:#fff;margin-bottom:4px}
  .card-back{left:610px;top:860px;width:180px;height:100px;background:var(--paper)}
  .card-back .brand{left:8px;right:auto;width:90px;top:22px;font-size:6px}
  .card-back .brand-dot{width:6px;height:6px;background:var(--ink);margin-bottom:4px}
  .card-info{position:absolute;left:102px;top:22px;width:76px;border-left:1px solid var(--rule);padding-left:6px;font-size:4.4px;line-height:1.5;color:var(--muted)}
  .card-name{font-size:5.6px;color:var(--ink);text-transform:uppercase;letter-spacing:.03em}
  .card-role{margin-bottom:6px}
  .card-info b{color:var(--ink)}
  .card-address{margin-top:5px;padding-top:4px;border-top:1px solid #ccc}
</style>
</head>
<body>

<section class="sheet folder">
  <div class="folder-spine"></div>
  <div class="brand"><span class="brand-dot"></span>Hollingsworth Hollingsworth Fenwicke</div>
  <div class="folder-web">www.TWVQX.example</div>
</section>

<section class="sheet letterhead">
  <div class="brand"><span class="brand-dot"></span>Hollingsworth Hollingsworth Fenwicke</div>
  <div class="letter-body">
    <p>Dear sir,</p>
    <p>Thank you for reaching out to our office regarding your recent matter. We have reviewed the documents you provided and prepared a short summary of the next steps. Our team will contact you within the week to arrange a meeting at a time that suits you.</p>
    <p>Please gather any records, letters or notes that relate to the events in question. Even small details can matter, and having them ready will help us give clear advice and move forward with care.</p>
    <p>Every conversation with our attorneys is kept private. If anything changes before we meet, simply call the office and a member of our staff will update your file right away.</p>
    <p>We appreciate the trust you have placed in our firm and look forward to working with you.</p>
    <div class="letter-close">Yours Sincerely,<strong>Lorna Pettigrew</strong></div>
  </div>
  <div class="signature" role="img" aria-label="Handwritten signature"></div>
  <div class="letter-footer">
    <div class="col">5182 North Pelham Avenue<br>Tulsa, Oklahoma 74219<br><b>Tel:</b> (918) 555-0143<br><b>Fax:</b> (918) 555-0187<br><b>Web:</b> www.TWVQX.example</div>
    <div class="col"><b>PARTNERS:</b><br>Dale K. Hollingsworth<br>Vernon P. Hollingsworth<br>Mark E. Fenwicke<br>Tyler D. Ashcombe</div>
    <div class="col"><b>STAFF:</b><br>Brenda K. Lyle<br>Tendaji K. Oyelowanta<br>Gordon Pettijo</div>
    <div class="col"><b>STAFF:</b><br>Hilda V. Pruitt, RN<br>Of Counsel:<br>Wendell S. Hollingsworth</div>
  </div>
</section>

<section class="sheet envelope-front">
  <div class="brand"><span class="brand-dot"></span>Hollingsworth Hollingsworth Fenwicke</div>
  <div class="envelope-address">5182 North Pelham Avenue<br>Tulsa, Oklahoma 74219</div>
</section>

<section class="sheet envelope-back">
  <svg width="467" height="80" viewBox="0 0 467 80" aria-hidden="true">
    <polygon class="envelope-flap" points="0,0 467,0 467,8 385,72 82,72 0,8" fill="var(--dark)"/>
  </svg>
  <div class="brand"><span class="brand-dot"></span>Hollingsworth Hollingsworth Fenwicke</div>
</section>

<section class="sheet card-front">
  <div class="brand"><span class="brand-dot"></span>Hollingsworth Hollingsworth Fenwicke</div>
</section>

<section class="sheet card-back">
  <div class="brand"><span class="brand-dot"></span>Hollingsworth Hollingsworth Fenwicke</div>
  <div class="card-info">
    <div class="card-name">Dale K. Hollingsworth</div>
    <div class="card-role">Partner</div>
    <b>Tel:</b> (918) 555-0143<br>
    <b>Fax:</b> (918) 555-0187<br>
    <b>Email:</b> dale@twvqx.example<br>
    <b>Web:</b> www.twvqx.example
    <div class="card-address">5182 North Pelham Avenue<br>Tulsa, Oklahoma 74219</div>
  </div>
</section>

</body>
</html>
```